fernbolt website

commerce website to sell cookeries, brackets, mailboxes and to show off homes built. Modern Steel in design see kelvo rides web page to be like: https://www.kelvorides.com/en/ sorry its blue mantis hosting word press divi

must be able to add products to page

Target Market(s)

mainly western states of U.S.

Industry/Entity Type

Building Product

Coding

Coded - Design and coding required

Number of Pages Required

3 page

Font styles to use
Sans Serif

Colors

Designer to choose colors to be used in the design.

Requirements
Must have
• customers to be able to order products from page
• blue mantis hosting word press divi

```html
<!DOCTYPE html>
<html lang="en">
<head>
<meta charset="utf-8">
<title>Fernbolt — Steel Cookery, Brackets & Mail Boxes</title>
<link rel="stylesheet" href="https://fonts.googleapis.com/css2?family=Barlow+Condensed:ital,wght@0,300;0,400;0,500;0,700;1,400;1,500;1,600&family=Roboto:wght@400;500;700&display=swap">
<style>
:root{
  --steel-blue:#4d6896;
  --steel-blue-dark:#3f5883;
  --ink:#111111;
  --night:#141414;
  --white:#ffffff;
  --muted:#8c8c8c;
  --body:#555555;
  --light:#e9edf3;
}
*{box-sizing:border-box;margin:0;padding:0}
html,body{width:1200px;height:3354px;overflow:hidden}
body{position:relative;background:var(--white);font-family:'Roboto',sans-serif;color:var(--ink)}
.abs{position:absolute}
.cond{font-family:'Barlow Condensed',sans-serif}

/* header */
.site-header{left:0;top:0;width:1200px;height:159px;background:var(--steel-blue)}
.brand{left:88px;top:48px;display:flex;align-items:center;gap:10px;color:var(--white);font-family:'Roboto',sans-serif;font-weight:500;font-size:30px;letter-spacing:1px}
.brand-dot{width:22px;height:22px;border-radius:50%;background:var(--white)}
.main-nav{left:372px;top:72px;display:flex;gap:0;font-family:'Barlow Condensed',sans-serif;font-style:italic;font-weight:500;font-size:20px;color:var(--white)}
.main-nav a{position:absolute;color:var(--white);text-decoration:none;white-space:nowrap}
.main-nav a.active{text-decoration:underline;text-underline-offset:5px}
.btn-register{left:910px;top:69px;width:101px;height:35px;border-radius:18px;background:var(--white);color:var(--ink);font-family:'Barlow Condensed',sans-serif;font-weight:500;font-size:17px;display:flex;align-items:center;justify-content:center}
.icon-ring{width:34px;height:34px;border:2px solid var(--white);border-radius:50%;display:flex;align-items:center;justify-content:center}

/* hero */
.hero{left:0;top:159px;width:1200px;height:653px;background:radial-gradient(ellipse at 50% 40%,#6a6a6a 0%,#3c3c3c 55%,#1f1f1f 100%)}
.hero-panel{left:299px;top:379px;width:602px;height:144px;background:rgba(10,10,10,.88);clip-path:polygon(4% 0,100% 0,96% 100%,0 100%)}
.hero-title{left:0;width:1200px;text-align:center;color:var(--white);font-family:'Barlow Condensed',sans-serif;font-style:italic;line-height:1}
.hero-link{left:511px;top:545px;color:var(--white);font-family:'Barlow Condensed',sans-serif;font-style:italic;font-weight:500;font-size:32px;display:flex;align-items:center;gap:14px}
.dot{width:13px;height:13px;border:2px solid var(--white);border-radius:50%;top:771px}
.dot.on{background:var(--white)}

/* categories */
.cat-tile{top:825px;width:384px;height:273px}
.cat-band{left:0;bottom:0;width:100%;height:46px;background:rgba(15,15,15,.85);display:flex;align-items:center;justify-content:space-between;padding:0 15px 0 18px}
.cat-name{color:var(--white);font-family:'Barlow Condensed',sans-serif;font-style:italic;font-weight:600;font-size:25px}
.cat-btn{background:var(--steel-blue);color:var(--white);font-size:9px;font-family:'Barlow Condensed',sans-serif;padding:7px 14px}

/* about */
.about{left:143px;top:1187px;width:901px;height:528px;background:repeating-linear-gradient(45deg,var(--steel-blue) 0 2px,#506c9a 2px 4px)}
.about-media{left:176px;top:1245px;width:391px;height:412px;background:linear-gradient(135deg,#8a3030 0%,#9aa3ad 45%,#c3c8ce 100%)}
.about-title{left:604px;top:1268px;color:var(--white);font-family:'Barlow Condensed',sans-serif;font-weight:300;font-size:56px;line-height:1}
.about-title b{font-weight:700;font-size:44px;letter-spacing:1px}
.rule{height:2px}
.about-copy{left:604px;top:1351px;width:402px;color:var(--white);font-family:'Roboto',sans-serif;font-size:11.2px;line-height:19.5px;text-align:justify}
.btn-outline{left:607px;top:1594px;width:128px;height:38px;border:1px solid var(--white);color:var(--white);font-family:'Barlow Condensed',sans-serif;font-style:italic;font-size:19px;display:flex;align-items:center;justify-content:center;gap:10px}

/* section heads */
.sec-mark{left:0;width:1200px;text-align:center;color:var(--steel-blue);font-family:'Roboto',sans-serif;font-weight:700;font-size:15px;letter-spacing:3px}
.sec-title{left:0;width:1200px;text-align:center;font-family:'Barlow Condensed',sans-serif;font-weight:300;font-size:54px;line-height:1;color:var(--ink)}
.sec-title b{font-weight:700}
.sec-rule{left:562px;width:66px;height:2px;background:var(--steel-blue)}

/* products */
.product{top:1947px;width:275px;height:383px;background:var(--steel-blue)}
.product-img{left:0;top:0;width:100%}
.product-name{left:0;width:100%;text-align:center;color:var(--white);font-family:'Barlow Condensed',sans-serif;font-size:25px}
.product-price{left:0;width:100%;text-align:center;color:var(--white);font-size:16px;font-family:'Roboto',sans-serif}
.product-price small{color:#c7d0de;font-size:14px;margin-right:6px}
.product-price s{color:#c7d0de;font-size:14px;margin-right:8px}
.btn-cart{left:83px;top:317px;width:109px;height:32px;border:1px solid var(--white);border-radius:16px;color:var(--white);font-size:13px;display:flex;align-items:center;justify-content:center}
.quick{width:32px;height:32px;border-radius:50%;display:flex;align-items:center;justify-content:center}
.tip{left:132px;top:16px;width:91px;height:24px;background:#1b1b1b;color:var(--white);font-size:11px;display:flex;align-items:center;justify-content:center}
.pager{top:2357px;height:38px;border:1px solid var(--ink);display:flex;align-items:center;justify-content:center}

/* blog */
.post-img{top:2608px;width:277px;height:163px}
.post-date{top:2784px;width:43px;height:86px}
.post-date .d{height:43px;background:var(--steel-blue);color:var(--white);text-align:center;font-family:'Barlow Condensed',sans-serif;font-size:18px;line-height:1;padding-top:5px}
.post-date .d small{display:block;font-size:9px;font-family:'Roboto',sans-serif}
.post-date .c{height:43px;background:#2a2a2a;color:var(--white);text-align:center;font-size:11px;padding-top:6px}
.post-title{top:2788px;font-family:'Roboto',sans-serif;font-weight:700;font-size:15.5px;color:#4a4a4a}
.post-copy{top:2816px;width:210px;font-size:10.4px;line-height:17px;color:#7a7a7a}
.post-more{top:2892px;font-family:'Barlow Condensed',sans-serif;font-style:italic;font-size:13px;color:#555;display:flex;gap:8px;align-items:center}

/* footer */
.site-footer{left:0;top:2981px;width:1200px;height:373px;background:var(--night)}
.foot-brand{left:147px;top:3080px;display:flex;align-items:center;gap:12px;color:var(--white);font-weight:500;font-size:34px;letter-spacing:1px}
.foot-about{left:143px;top:3180px;width:305px;color:#d7d7d7;font-size:10.8px;line-height:17px}
.foot-head{top:3047px;color:var(--white);font-family:'Barlow Condensed',sans-serif;font-size:25px}
.foot-rule{top:3085px;width:38px;height:2px;background:var(--steel-blue)}
.foot-list{list-style:none;color:var(--white);font-family:'Barlow Condensed',sans-serif;font-size:11px}
.foot-list li{position:absolute;white-space:nowrap}
.contact{color:var(--white);font-size:11px;line-height:21px}
.foot-divider{left:143px;top:3299px;width:901px;height:1px;background:#2f2f2f}
.copyright{left:0;top:3319px;width:1200px;text-align:center;color:var(--white);font-size:11px;display:flex;justify-content:center;align-items:center;gap:12px}
.social{width:17px;height:17px;border-radius:50%;background:#9a9a9a;display:inline-block}
</style>
</head>
<body>

<header class="abs site-header">
  <div class="abs brand"><span class="brand-dot"></span>FERNBOLT</div>
  <nav class="abs main-nav" style="left:0;top:72px">
    <a class="active" style="left:372px">HOME</a>
    <a style="left:446px">PRODUCTS</a>
    <a style="left:554px">HOMES BUILT</a>
    <a style="left:677px">ABOUT</a>
    <a style="left:759px">CONTACT</a>
  </nav>
  <div class="abs btn-register">REGISTER</div>
  <div class="abs icon-ring" style="left:1023px;top:70px">
    <svg width="14" height="16" viewBox="0 0 14 16"><rect x="1" y="7" width="12" height="9" rx="1" fill="#fff"/><path d="M4 7V4.5a3 3 0 0 1 6 0V7" stroke="#fff" stroke-width="2" fill="none"/></svg>
  </div>
  <div class="abs icon-ring" style="left:1068px;top:70px">
    <svg width="17" height="15" viewBox="0 0 17 15"><path d="M1 1h3l2 8h8l2-6H5" stroke="#fff" stroke-width="1.8" fill="none"/><circle cx="7" cy="13" r="1.5" fill="#fff"/><circle cx="13" cy="13" r="1.5" fill="#fff"/></svg>
  </div>
</header>

<section class="abs hero" role="img" aria-label="Warehouse stacked with rolled steel coils"></section>
<div class="abs hero-panel"></div>
<div class="abs hero-title" style="top:400px;font-weight:400;font-size:52px">LOREM IPSUM DOLOR</div>
<div class="abs hero-title" style="top:452px;font-weight:600;font-size:54px">SIT AMET, CONSECTETUR</div>
<div class="abs hero-link">READ MORE
  <svg width="44" height="14" viewBox="0 0 44 14"><path d="M0 7h42M35 1l7 6-7 6" stroke="#fff" stroke-width="2.5" fill="none"/></svg>
</div>
<span class="abs dot" style="left:550px"></span>
<span class="abs dot" style="left:576px"></span>
<span class="abs dot on" style="left:602px"></span>
<span class="abs dot" style="left:630px"></span>

<div class="abs cat-tile" style="left:10px;background:linear-gradient(135deg,#7a5234,#b9b9b9 60%,#3a3a3a)" role="img" aria-label="Steel pots and pans on a wooden table">
  <div class="abs cat-band"><span class="cat-name">STEEL COOKERY</span><span class="cat-btn">READ MORE</span></div>
</div>
<div class="abs cat-tile" style="left:407px;background:linear-gradient(135deg,#d6d6d6,#8f8f8f 60%,#5f5f5f)" role="img" aria-label="Galvanised steel angle brackets with screws">
  <div class="abs cat-band"><span class="cat-name">BRACKETS</span><span class="cat-btn">READ MORE</span></div>
</div>
<div class="abs cat-tile" style="left:804px;background:linear-gradient(135deg,#e0d9c7,#c43a3a 55%,#4f7a3a)" role="img" aria-label="Red mailbox beside garden steps">
  <div class="abs cat-band"><span class="cat-name">MAIL BOXES</span><span class="cat-btn">READ MORE</span></div>
</div>

<section class="abs about"></section>
<div class="abs about-media" role="img" aria-label="Collage of a red mailbox, steel cookware and stacked steel brackets"></div>
<h2 class="abs about-title">ABOUT <b>FERNBOLT</b></h2>
<div class="abs rule" style="left:604px;top:1329px;width:66px;background:#fff"></div>
<p class="abs about-copy">Lorem ipsum dolor sit amet, consectetur adipiscing elit, sed do eiusmod tempor incididunt ut labore et dolore magna aliqua. Ut enim ad minim veniam, quis nostrud exercitation ullamco laboris nisi ut aliquip ex ea commodo consequat. Duis aute irure dolor in reprehenderit in voluptate velit esse cillum dolore eu fugiat nulla pariatur. Excepteur sint occaecat cupidatat non proident, sunt in culpa qui officia deserunt mollit anim id est laborum.Lorem ipsum dolor sit amet, consectetur adipiscing elit, sed do eiusmod tempor incididunt ut labore et dolore magna aliqua. Ut enim ad minim veniam, quis nostrud exercitation ullamco laboris nisi ut aliquip ex ea commodo consequat. Duis aute irure dolor in reprehenderit in voluptate velit esse cillum dolore eu fugiat nulla pariatur. Excepteur sint occaecat cupidatat non proident, sunt in culpa qui officia deserunt mollit anim id est laborum.</p>
<div class="abs btn-outline">READ MORE
  <svg width="26" height="10" viewBox="0 0 26 10"><path d="M0 5h24M19 1l5 4-5 4" stroke="#fff" stroke-width="1.5" fill="none"/></svg>
</div>

<div class="abs sec-mark" style="top:1818px">FERNBOLT</div>
<h2 class="abs sec-title" style="top:1856px">FEATURED <b>PRODUCTS</b></h2>
<div class="abs sec-rule" style="top:1916px"></div>

<article class="abs product" style="left:143px">
  <div class="abs product-img" style="height:272px;background:linear-gradient(160deg,#f2f2f2,#9a9a9a 55%,#3a3a3a)" role="img" aria-label="Stacked steel cookware"></div>
  <div class="abs product-name" style="top:300px">PRODUCTNAME</div>
  <div class="abs product-price" style="top:336px"><small>Price</small><s>$ 0.00</s>$ 0.00</div>
</article>
<article class="abs product" style="left:456px">
  <div class="abs product-img" style="height:207px;background:linear-gradient(180deg,#6d6d6d,#474747 60%,#8c8c8c)" role="img" aria-label="Black steel mailbox with red flag"></div>
  <div class="abs tip">Add to Wishlist</div>
  <div class="abs quick" style="left:232px;top:11px;background:#1b1b1b">
    <svg width="14" height="13" viewBox="0 0 14 13"><path d="M7 12 1.5 6.5A3.2 3.2 0 0 1 7 2a3.2 3.2 0 0 1 5.5 4.5Z" fill="#fff"/></svg>
  </div>
  <div class="abs quick" style="left:232px;top:52px;background:#2b2b2b">
    <svg width="14" height="10" viewBox="0 0 14 10"><ellipse cx="7" cy="5" rx="6" ry="4" fill="none" stroke="#fff" stroke-width="1.5"/><circle cx="7" cy="5" r="1.8" fill="#fff"/></svg>
  </div>
  <div class="abs quick" style="left:232px;top:93px;background:#2b2b2b">
    <svg width="13" height="13" viewBox="0 0 13 13"><circle cx="5.5" cy="5.5" r="4" fill="none" stroke="#fff" stroke-width="1.5"/><path d="M8.5 8.5l3.5 3.5" stroke="#fff" stroke-width="1.5"/></svg>
  </div>
  <div class="abs product-name" style="top:235px">PRODUCTNAME</div>
  <div class="abs product-price" style="top:271px"><small>Price</small><s>$ 0.00</s>$ 0.00</div>
  <div class="abs btn-cart">ADD TO CART</div>
</article>
<article class="abs product" style="left:769px">
  <div class="abs product-img" style="height:272px;background:linear-gradient(160deg,#dcdcdc,#b4b4b4 55%,#e9e9e9)" role="img" aria-label="Assorted perforated steel brackets"></div>
  <div class="abs product-name" style="top:300px">PRODUCTNAME</div>
  <div class="abs product-price" style="top:336px"><small>Price</small><s>$ 0.00</s>$ 0.00</div>
</article>

<div class="abs pager" style="left:498px;width:28px">
  <svg width="10" height="18" viewBox="0 0 10 18"><path d="M8 1 1 9l7 8" stroke="#111" stroke-width="1.5" fill="none"/></svg>
</div>
<div class="abs pager cond" style="left:531px;width:128px;gap:16px;font-style:italic;font-size:17px">VIEW ALL
  <svg width="26" height="10" viewBox="0 0 26 10"><path d="M0 5h24M19 1l5 4-5 4" stroke="#111" stroke-width="1.5" fill="none"/></svg>
</div>
<div class="abs pager" style="left:664px;width:28px;background:var(--ink)">
  <svg width="10" height="18" viewBox="0 0 10 18"><path d="M2 1l7 8-7 8" stroke="#fff" stroke-width="1.5" fill="none"/></svg>
</div>

<div class="abs sec-mark" style="top:2478px">FERNBOLT</div>
<h2 class="abs sec-title" style="top:2517px">LATEST <b>BLOG</b></h2>
<div class="abs sec-rule" style="top:2577px"></div>

<div class="abs post-img" style="left:156px;background:linear-gradient(135deg,#2a5aa8,#3e6fbf 55%,#9aa0a8)" role="img" aria-label="Door closer bracket on a blue door"></div>
<div class="abs post-img" style="left:456px;background:linear-gradient(180deg,#7c8084,#4a4d50 60%,#2c2c2c)" role="img" aria-label="Vintage mailbox set in a wrought iron gate"></div>
<div class="abs post-img" style="left:754px;background:linear-gradient(180deg,#4a4a4a,#a89a7a 50%,#2a2a2a)" role="img" aria-label="Hanging steel pots in a commercial kitchen"></div>

<div class="abs post-date" style="left:156px"><div class="d">31<small>JAN</small></div><div class="c">&#9679;<br>0</div></div>
<h3 class="abs post-title" style="left:221px">Lorem ipsum dolor sit amet</h3>
<p class="abs post-copy" style="left:221px">sed do eiusmod tempor incididunt ut labore et dolore magna aliqua. Ut enim ad minim veniam, quis nostrud exercitation ullamco laboris nisi ut aliquip ...</p>
<div class="abs post-more" style="left:225px">READ MORE <svg width="20" height="8" viewBox="0 0 20 8"><path d="M0 4h18M14 1l4 3-4 3" stroke="#555" fill="none"/></svg></div>

<div class="abs post-date" style="left:456px"><div class="d">31<small>JAN</small></div><div class="c">&#9679;<br>0</div></div>
<h3 class="abs post-title" style="left:521px;color:var(--steel-blue)">Lorem ipsum dolor sit amet</h3>
<p class="abs post-copy" style="left:521px">sed do eiusmod tempor incididunt ut labore et dolore magna aliqua. Ut enim ad minim veniam, quis nostrud exercitation ullamco laboris nisi ut aliquip ...</p>
<div class="abs post-more" style="left:521px;color:var(--steel-blue)">READ MORE <svg width="20" height="8" viewBox="0 0 20 8"><path d="M0 4h18M14 1l4 3-4 3" stroke="#4d6896" fill="none"/></svg></div>

<div class="abs post-date" style="left:754px"><div class="d">31<small>JAN</small></div><div class="c">&#9679;<br>0</div></div>
<h3 class="abs post-title" style="left:819px">Lorem ipsum dolor sit amet</h3>
<p class="abs post-copy" style="left:819px">sed do eiusmod tempor incididunt ut labore et dolore magna aliqua. Ut enim ad minim veniam, quis nostrud exercitation ullamco laboris nisi ut aliquip ...</p>
<div class="abs post-more" style="left:819px">READ MORE <svg width="20" height="8" viewBox="0 0 20 8"><path d="M0 4h18M14 1l4 3-4 3" stroke="#555" fill="none"/></svg></div>

<footer class="abs site-footer"></footer>
<div class="abs foot-brand"><span class="brand-dot"></span>FERNBOLT</div>
<p class="abs foot-about">Lorem ipsum dolor sit amet, consectetur adipiscing elit, sed do eiusmod tempor incididunt ut labore et dolore magna aliqua. Ut enim ad minim veniam, quis nostrud exercitation ullamco laboris nisi ut aliquip ex ea commodo consequat.</p>

<h4 class="abs foot-head" style="left:522px">QUICK LINKS</h4>
<div class="abs foot-rule" style="left:522px"></div>
<ul class="foot-list">
  <li style="left:523px;top:3108px">HOME</li>
  <li style="left:523px;top:3138px">PRODUCTS</li>
  <li style="left:523px;top:3168px">HOMES BUILT</li>
  <li style="left:523px;top:3198px">ABOUT</li>
  <li style="left:523px;top:3228px">CONTACT</li>
</ul>

<h4 class="abs foot-head" style="left:707px">PRODUCTS</h4>
<div class="abs foot-rule" style="left:707px"></div>
<ul class="foot-list">
  <li style="left:708px;top:3108px">PRODUCT 1</li>
  <li style="left:708px;top:3138px">PRODUCT 2</li>
  <li style="left:708px;top:3168px">PRODUCT 3</li>
  <li style="left:708px;top:3198px">PRODUCT 4</li>
  <li style="left:708px;top:3228px">PRODUCT 5</li>
</ul>

<h4 class="abs foot-head" style="left:893px">CONTACT DETAILS</h4>
<div class="abs foot-rule" style="left:893px"></div>
<svg class="abs" style="left:892px;top:3112px" width="14" height="18" viewBox="0 0 14 18"><path d="M7 17s6-6.5 6-10.5A6 6 0 0 0 1 6.5C1 10.5 7 17 7 17Z" fill="#4d6896"/><circle cx="7" cy="6.5" r="2.2" fill="#141414"/></svg>
<div class="abs contact" style="left:923px;top:3108px">123 Building Name, Area<br>Name, Street,City,Country</div>
<svg class="abs" style="left:892px;top:3162px" width="14" height="14" viewBox="0 0 14 14"><path d="M3 1l2.5 3-1.5 2a8 8 0 0 0 4 4l2-1.5 3 2.5-1.5 2C6 13 1 8 1 2.5Z" fill="#4d6896"/></svg>
<div class="abs contact" style="left:923px;top:3160px">123-456-7890</div>
<svg class="abs" style="left:891px;top:3198px" width="16" height="14" viewBox="0 0 16 14"><path d="M15 1 1 6.5l5 2 1.5 4.5 2.5-3.5 3.5 2.5Z" fill="#4d6896"/></svg>
<div class="abs contact" style="left:925px;top:3194px">hello@fernbolt.com</div>

<div class="abs foot-divider"></div>
<div class="abs copyright">Copyright &copy; 2020 FERNBOLT. All rights reserved.
  <span><span class="social"></span> <span class="social"></span> <span class="social"></span></span>
</div>

</body>
</html>
```